Custom Office Whiteboard for Staff

I need a custom whiteboard layout design. All fields are contained in the attached images along with artwork requirements including required bleed. Size will be 1200mm x 900mm.

Feel free to make is more visually appealing than this draft.

Use colors blue, black and white to keep company feel.

Font styles to use
Sans Serif

Colors
ffffff
000000
33a6d7

```html
<!DOCTYPE html>
<html lang="en">
<head>
<meta charset="utf-8">
<title>Skyward Ballooning – Staff Whiteboard</title>
<link rel="stylesheet" href="https://fonts.googleapis.com/css2?family=Catamaran:wght@400;500;600;700&display=swap">
<style>
:root{
  --blue:#08a9e8;
  --ink:#000000;
  --paper:#ffffff;
  --header-grey:#f3f3f3;
  --bar-dark:#3d3d3d;
  --rule:#c9c9c9;
  --text:#1a1a1a;
}
*{box-sizing:border-box;margin:0;padding:0}
html,body{width:1200px;height:918px;overflow:hidden;background:var(--paper)}
body{font-family:"Catamaran",sans-serif;color:var(--text);position:relative}
.top-strip{position:absolute;left:0;top:0;width:1200px;height:25px;background:var(--header-grey)}
.brand-panel{position:absolute;left:0;top:0;width:1200px;height:180px}
.brand-name{position:absolute;left:70px;top:76px;display:flex;align-items:center;gap:12px;font-size:34px;font-weight:700;color:var(--ink);letter-spacing:.5px}
.brand-dot{width:26px;height:26px;border-radius:50%;background:var(--blue)}
.contact{position:absolute;left:527px;top:56px;font-size:20px;line-height:1;color:var(--ink)}
.contact li{list-style:none;display:flex;align-items:center;gap:10px;height:32px}
.contact svg{width:18px;height:18px;flex:none}
.company{position:absolute;left:899px;top:58px;font-size:19.5px;line-height:1.25;color:var(--ink)}
.company .gap{margin-top:6px}
.panel-head{background:var(--blue);color:var(--paper);text-align:center;font-weight:500}
table{border-collapse:collapse;width:100%;table-layout:fixed}
th{background:var(--bar-dark);color:var(--paper);font-weight:500;border-right:1px solid #5a5a5a}
th:last-child{border-right:none}
td{border:1px solid var(--rule);text-align:center;color:var(--ink)}
.crew{position:absolute;left:53px;top:197px;width:797px}
.crew .panel-head{height:39px;font-size:22px;line-height:41px}
.crew th{height:35px;font-size:13.5px;line-height:1}
.crew td{height:29.6px}
.notes{position:absolute;left:915px;top:197px;width:231px;height:429px;border:2px solid #cfcfcf;border-radius:0 0 6px 6px}
.notes .panel-head{position:relative;margin:-2px -2px 0;height:56px;font-size:31px;line-height:62px}
.notes .panel-head::after{content:"";position:absolute;left:50%;bottom:-10px;margin-left:-10px;border:10px solid transparent;border-bottom:none;border-top-color:var(--blue)}
.task{position:absolute;top:645px}
.task .panel-head{height:29px;font-size:15px;line-height:31px}
.task th{height:24px;font-size:13.5px}
.task td{height:24.2px;font-size:11px}
.six{left:53px;width:266px}
.twelve{left:343px;width:266px}
.schedule{left:634px;width:513px}
.foot-blue{position:absolute;left:0;top:910px;width:530px;height:8px;background:var(--blue)}
.foot-dark{position:absolute;left:524px;top:910px;width:676px;height:8px;background:#1d1d1d;clip-path:polygon(6px 0,100% 0,100% 100%,0 100%)}
</style>
</head>
<body>
<div class="top-strip"></div>
<svg class="brand-panel" viewBox="0 0 1200 180" aria-hidden="true">
  <polygon points="0,25 523,25 427,180 0,180" fill="#f3f3f3"/>
  <polygon points="515,25 525,25 429,156 419,156" fill="#08a9e8"/>
</svg>
<div class="brand-name"><span class="brand-dot"></span>Skyward Ballooning</div>

<ul class="contact">
  <li><svg viewBox="0 0 18 18"><rect x="1.5" y="4" width="15" height="10" fill="none" stroke="#08a9e8" stroke-width="1.4"/><path d="M1.5 4l7.5 6 7.5-6" fill="none" stroke="#08a9e8" stroke-width="1.4"/></svg>hello@skywardballooning.com.au</li>
  <li><svg viewBox="0 0 18 18"><circle cx="9" cy="9" r="7.5" fill="none" stroke="#08a9e8" stroke-width="1.4"/><ellipse cx="9" cy="9" rx="3.2" ry="7.5" fill="none" stroke="#08a9e8" stroke-width="1.2"/><path d="M1.5 9h15M3 5h12M3 13h12" stroke="#08a9e8" stroke-width="1.1"/></svg>www.skywardballooning.com.au</li>
  <li><svg viewBox="0 0 18 18"><circle cx="9" cy="9" r="7.5" fill="none" stroke="#08a9e8" stroke-width="1.4"/><path d="M6.3 5.2l1.4-.4.9 2-1 .8c.5 1.2 1.3 2 2.5 2.6l.8-1 2 .9-.4 1.4c-3.5.2-6.4-2.6-6.2-6.3z" fill="#08a9e8"/></svg>1300 555 019</li>
</ul>

<div class="company">
  <div>Southern Skycraft Pty Ltd</div>
  <div>T/A Skyward Ballooning</div>
  <div class="gap">CASA AOC: S518204</div>
  <div>Certificate of Approval: 4816</div>
</div>

<section class="crew">
  <div class="panel-head">FLIGHT / GROUND CREW</div>
  <table>
    <tr><th>Crew Name</th><th>License Class</th><th>Medical</th><th>BFR</th><th>Instructor<br>Rating</th><th>CAO 20.11</th><th>DAMP</th><th>Maintenance<br>Authority</th><th>ASIC</th></tr>
    <tr><td></td><td></td><td></td><td></td><td></td><td></td><td></td><td></td><td></td></tr>
    <tr><td></td><td></td><td></td><td></td><td></td><td></td><td></td><td></td><td></td></tr>
    <tr><td></td><td></td><td></td><td></td><td></td><td></td><td></td><td></td><td></td></tr>
    <tr><td></td><td></td><td></td><td></td><td></td><td></td><td></td><td></td><td></td></tr>
    <tr><td></td><td></td><td></td><td></td><td></td><td></td><td></td><td></td><td></td></tr>
    <tr><td></td><td></td><td></td><td></td><td></td><td></td><td></td><td></td><td></td></tr>
    <tr><td></td><td></td><td></td><td></td><td></td><td></td><td></td><td></td><td></td></tr>
    <tr><td></td><td></td><td></td><td></td><td></td><td></td><td></td><td></td><td></td></tr>
    <tr><td></td><td></td><td></td><td></td><td></td><td></td><td></td><td></td><td></td></tr>
    <tr><td></td><td></td><td></td><td></td><td></td><td></td><td></td><td></td><td></td></tr>
    <tr><td></td><td></td><td></td><td></td><td></td><td></td><td></td><td></td><td></td></tr>
    <tr><td></td><td></td><td></td><td></td><td></td><td></td><td></td><td></td><td></td></tr>
  </table>
</section>

<section class="notes">
  <div class="panel-head">NOTES</div>
</section>

<section class="task six">
  <div class="panel-head">6 MONTHLY TASKS</div>
  <table>
    <colgroup><col style="width:67%"><col></colgroup>
    <tr><th>Task</th><th>Due Date</th></tr>
    <tr><td>Operations Manual</td><td></td></tr>
    <tr><td>Staff Meeting</td><td></td></tr>
    <tr><td>SMS Meeting</td><td></td></tr>
    <tr><td>Fire Extinguisher Inspection</td><td></td></tr>
    <tr><td>Flight Instrument Inspection</td><td></td></tr>
    <tr><td></td><td></td></tr>
    <tr><td></td><td></td></tr>
    <tr><td></td><td></td></tr>
  </table>
</section>

<section class="task twelve">
  <div class="panel-head">12 MONTHLY TASKS</div>
  <table>
    <tr><th>Task</th><th>Due Date</th></tr>
    <tr><td>COA Internal Audit</td><td></td></tr>
    <tr><td>SMS Audit</td><td></td></tr>
    <tr><td>Fatigue Training</td><td></td></tr>
    <tr><td>CAO 20.11</td><td></td></tr>
    <tr><td></td><td></td></tr>
    <tr><td></td><td></td></tr>
    <tr><td></td><td></td></tr>
    <tr><td></td><td></td></tr>
  </table>
</section>

<section class="task schedule">
  <div class="panel-head">BALLOON ANNUAL / PERIODIC SCHEDULE</div>
  <table>
    <tr><th>Balloon</th><th>Type</th><th>Annual Date</th><th>Periodic Time</th></tr>
    <tr><td>VH-QRA</td><td>Lyn D90</td><td></td><td></td></tr>
    <tr><td>VH-QRB</td><td>Lyn E180</td><td></td><td></td></tr>
    <tr><td>VH-QRC</td><td>Lyn E240</td><td></td><td></td></tr>
    <tr><td>VH-QRD</td><td>Lyn B400</td><td></td><td></td></tr>
    <tr><td>VH-QRE</td><td>Lyn G450</td><td></td><td></td></tr>
    <tr><td></td><td></td><td></td><td></td></tr>
    <tr><td></td><td></td><td></td><td></td></tr>
    <tr><td></td><td></td><td></td><td></td></tr>
  </table>
</section>

<div class="foot-blue"></div>
<div class="foot-dark"></div>
</body>
</html>
```